Visitenkarten für Wahlärztin
Zielgruppe
Ich bin Ärztin für Allgemeinmedizin. Mein Schwerpunkt liegt auf Akupunktur und Manuelle Medizin. Als Wahlärztin sind meine Zielgruppe Privatpatienten - Primär Erwachsene, aber auch Kinder.
Aufgabenstellung
Logo (ev. nur Zeichen) und Informationen auf der Visitenkarte:
Dr. Gerlinde Wampetsreiter
Ärztin für Allgemeinmedizin
Akupunktur
Manuelle Medizin
Lerchenfeldgasse 7
3519 Lindenau am Auberg
praxis@dr-wampetsreiter.at
www.dr-wampetsreiter.at
Wahlärztin
Termin nach telefonischer Vereinbarung
Das Design soll das edle Logo mit Natürlichkeit/Leichtigkeit verbinden bzw. erden und ganzheitliche Medizin im verkörpern.

```html
<!DOCTYPE html>
<html lang="de">
<head>
<meta charset="utf-8">
<title>Visitenkarte – Dr. Gerlinde Wampetsreiter</title>
<link rel="stylesheet" href="https://fonts.googleapis.com/css2?family=Cabin:wght@400;500&display=swap">
<style>
  :root {
    --backdrop: #d9dadb;
    --card: #ffffff;
    --charcoal: #3c3c3c;
    --ink: #4a4a4a;
    --gold: #c9a227;
    --gold-deep: #b8891b;
    --gold-band: #d3ae34;
  }
  * { box-sizing: border-box; margin: 0; padding: 0; }
  html, body {
    width: 1200px; height: 745px; overflow: hidden;
    background: var(--backdrop);
    font-family: "Cabin", sans-serif;
    color: var(--ink);
  }
  .sheet { position: relative; width: 1200px; height: 745px; }
  .card {
    position: absolute; top: 210px;
    width: 500px; height: 324px;
    background: var(--card);
    box-shadow: 0 4px 14px rgba(0,0,0,0.18);
    overflow: hidden;
  }
  .card--front { left: 70px; }
  .card--back { left: 630px; }

  .card__band-bottom {
    position: absolute; left: 0; right: 0; bottom: 0;
    height: 5px; background: var(--gold-band);
  }
  .card__header { position: absolute; left: 0; top: 0; }

  .back-band {
    position: absolute; left: 0; top: 0; right: 0;
    height: 27px; background: var(--charcoal);
  }
  .back-band-line {
    position: absolute; left: 0; right: 0; top: 30px;
    height: 1px; background: var(--gold);
  }

  .brand {
    position: absolute;
    display: flex; align-items: center; gap: 7px;
    font-size: 15px; font-weight: 500; color: var(--charcoal);
    letter-spacing: 0.02em; white-space: nowrap;
  }
  .brand__dot {
    width: 10px; height: 10px; border-radius: 50%;
    background: var(--gold);
  }
  .brand--corner { right: 14px; top: 52px; }
  .brand--center { left: 0; right: 0; justify-content: center; }
  .card--front .brand--center { top: 132px; }
  .card--back .brand--center { top: 96px; }

  .name {
    position: absolute; left: 0; right: 0; top: 176px;
    text-align: center;
    font-size: 26px; font-weight: 500;
    color: var(--gold-deep);
    letter-spacing: 0.01em;
  }
  .rule {
    position: absolute; left: 44px; right: 44px;
    height: 1.5px; background: var(--gold);
  }
  .card--front .rule { top: 214px; }
  .card--back .rule { top: 210px; }

  .lines {
    position: absolute; left: 0; right: 0;
    text-align: center; color: var(--ink);
  }
  .lines--specialty { top: 223px; font-size: 16.5px; line-height: 22px; }
  .lines--status { top: 157px; font-size: 13.5px; line-height: 21px; }
  .lines--contact { top: 225px; font-size: 13.5px; line-height: 21px; letter-spacing: 0.02em; }
</style>
</head>
<body>
<main class="sheet">

  <section class="card card--front" aria-label="Vorderseite">
    <svg class="card__header" width="500" height="60" viewBox="0 0 500 60">
      <path d="M0 0 H408 Q392 12 384 36 H0 Z" fill="var(--charcoal)"/>
      <rect x="0" y="38.5" width="381" height="1" fill="var(--gold)"/>
    </svg>
    <div class="brand brand--corner"><span class="brand__dot"></span>Wampetsreiter</div>
    <div class="brand brand--center"><span class="brand__dot"></span>Wampetsreiter</div>
    <h1 class="name">Dr. Gerlinde Wampetsreiter</h1>
    <div class="rule"></div>
    <p class="lines lines--specialty">Ärztin für Allgemeinmedizin<br>Akupunktur ○ Manuelle Medizin</p>
    <div class="card__band-bottom"></div>
  </section>

  <section class="card card--back" aria-label="Rückseite">
    <div class="back-band"></div>
    <div class="back-band-line"></div>
    <div class="brand brand--center"><span class="brand__dot"></span>Wampetsreiter</div>
    <p class="lines lines--status">Wahlärztin<br>Termin nach telefonischer Vereinbarung</p>
    <div class="rule"></div>
    <p class="lines lines--contact">Lerchenfeldgasse 7 ○ 3519 Lindenau am Auberg<br>Tel. +43 677 208 31 470<br>praxis@dr-wampetsreiter.at ○ www.dr-wampetsreiter.at</p>
    <div class="card__band-bottom"></div>
  </section>

</main>
</body>
</html>
```